Zielgruppe
Wir sind die Kreisverwaltung des Landkreises Darmstadt-Dieburg (das Landratsamt), kurz KoWeFa genannt. Wir möchten unsere rund 1.800 Mitarbeiter auf das neue Mitarbeitermagazin, das es seit Kurzem online gibt, aufmerksam machen.
Aufgabenstellung
Der KoWeFa möchte zunehmend das verstaubte Image einer Behörde ablegen und als modern wahrgenommen werden. Es besteht der Wunsch, sich von anderen Landkreisen und Ämtern positiv abzuheben. Man möchte auf sich aufmerksam machen, ungewöhnliche Akzente setzen und mit Gegensätzen spielen. Überraschen und dabei authentisch sein.
POSTKARTENFORMAT DIN LANG (105 x 210):
Für die Vorderseite dachten wir an eine (regenbogen-)bunte Einhorn-Maske (Bastelbild). Vorschlag: Die Augen könnten mit gestrichelten Linien und Scherensymbol als Fläche zum Ausschneiden gekennzeichnet werden. Die Nase könnte regenbogenfarbig gestaltet und ebenfalls mit Schneidelinien markiert werden. Einmal ausgeschnitten bietet die Stelle Platz für die Nase und das dreieckige Stück Pappe kann mit Klebolin oder Kleber als Horn oben an der Karte/Maske befestigt werden. Möglicherweise fallen Ihnen noch weitere Möglichkeiten ein. Hinweise zum Bastelvorgang müssten evtl. noch unauffällig auf der Karte platziert werden, da der Vorgang vermutlich (zumindest nicht völlig) selbsterklärend sein wird. Auch die Rückseite wird noch Platz für eine Anleitung bieten.
Vielleicht könnte man auch noch kleine Löcher an den Seiten andeuten, wo Gummibänder befestigt werden könnten.
Das Einhorn ist ein interner Gag und wird wiedererkannt und verstanden.
Das Design soll uns als druckfähige Datei im Postkarten-Format DIN lang (105 x 210) zugehen, das sich über Papier-Blitz oder Satz-und-Bogen produzieren lässt. Bitte integrieren Sie, wenn möglich, keine kostenpflichtigen Bilder oder Schriftarten.
TEXT VORDERSEITE:
Glaubst Du noch oder weißt Du schon, was es mit dem Einhorn auf sich hat?
TEXT RÜCKSEITE:
Lesen, was den KoWeFa bewegt. Die Rundblick gibt es jetzt online:
rundblick.kowefa-beispiel.de
Aktuelle Themen aus dem Landkreis und der Kreisverwaltung – auch von Zuhause, unterwegs oder mit dem Smartphone..

```html
<!DOCTYPE html>
<html lang="de">
<head>
<meta charset="utf-8">
<title>Rundblick KoWeFa – Postkarte Rückseite</title>
<link href="https://fonts.googleapis.com/css2?family=Nunito:wght@400;600;700&display=swap" rel="stylesheet">
<style>
  :root {
    --backdrop: #6f6f6f;
    --paper: #ffffff;
    --brand-blue: #1b3a8c;
    --logo-blue: #163f93;
    --band-blue: #dde9f8;
    --step-dot: #c7e2f7;
    --ink: #1f1f1f;
    --violet: #6a2286;
    --sky: #3aa8e0;
    --green: #95c11f;
    --yellow: #ffdd00;
    --orange: #f39200;
    --red: #e3312b;
  }
  * { box-sizing: border-box; margin: 0; padding: 0; }
  html, body { width: 1119px; height: 1200px; overflow: hidden; }
  body { background: var(--backdrop); font-family: "Nunito", sans-serif; position: relative; }

  .postcard {
    position: absolute; left: 141px; width: 851px; height: 425px;
    background: var(--paper); overflow: hidden;
  }
  .postcard--rainbow { top: 121px; }
  .postcard--plain { top: 640px; }

  .headline {
    position: absolute; left: 48px; width: 583px; top: 34px;
    text-align: center; color: var(--brand-blue);
    font-weight: 600; font-size: 19px; line-height: 29px; text-transform: uppercase;
  }
  .url-band {
    position: absolute; left: 48px; width: 583px; top: 96px; height: 35px;
    background: var(--band-blue); color: var(--brand-blue);
    font-size: 21px; line-height: 35px; text-align: center;
  }
  .lead {
    position: absolute; left: 48px; width: 583px; top: 143px;
    text-align: center; color: var(--ink); font-weight: 700;
    font-size: 13.2px; line-height: 19px;
  }
  .body-copy {
    position: absolute; left: 40px; width: 599px; top: 187px;
    text-align: center; color: var(--ink); font-size: 13.6px; line-height: 18.5px;
  }
  .body-copy p + p { margin-top: 8.5px; }

  .mask-illustration {
    position: absolute; border-radius: 40% 40% 45% 45%;
    background: linear-gradient(90deg, #f4f4f4 0%, #e9e2f0 25%, #e5f1d8 50%, #fff3c2 70%, #f6e1d6 100%);
  }
  .step {
    position: absolute; top: 378px; display: flex; align-items: center;
    font-size: 11px; color: var(--ink); white-space: nowrap;
  }
  .step__num {
    display: inline-flex; width: 21px; height: 21px; border-radius: 50%;
    background: var(--step-dot); align-items: center; justify-content: center;
    margin-right: 1px; font-size: 11px;
  }

  .brand-square {
    position: absolute; left: 708px; top: 41px; width: 102px; height: 102px;
    background: var(--logo-blue);
  }
  .wordmark {
    position: absolute; right: 41px; text-align: right;
    color: var(--brand-blue); font-weight: 700; line-height: 1;
  }
  .postcard--rainbow .wordmark { top: 324px; font-size: 30px; }
  .postcard--plain .wordmark { top: 344px; font-size: 24px; }

  .rainbow-bar { position: absolute; left: 0; bottom: 0; width: 851px; height: 17px; }
</style>
</head>
<body>

  <section class="postcard postcard--rainbow">
    <h1 class="headline">Lesen, was den KoWeFa bewegt.<br>Die Rundblick gibt es jetzt online:</h1>
    <div class="url-band">rundblick.kowefa-beispiel.de</div>
    <p class="lead">Aktuelle Themen aus dem Landkreis und der Kreisverwaltung – auch von Zuhause,<br>unterwegs oder mit dem Smartphone abrufbar</p>
    <div class="body-copy">
      <p>Einfach Einhorn-Maske basteln, aufsetzen und den KoWeFa aus anderem Rundblick sehen.<br>Schickt uns Eure Fotos mit Einhorn-Maske an rundblick@kowefa-beispiel.de</p>
      <p>Mehr Einhorn-Masken gefällig? Die Bastelvorlage gibt es auch online.</p>
    </div>

    <div class="mask-illustration" role="img" aria-label="Einhorn-Maske mit Regenbogenmähne, ausgeschnitten" style="left:74px;top:300px;width:112px;height:72px;"></div>
    <div class="mask-illustration" role="img" aria-label="Einhorn-Maske, goldenes Horn wird von hinten aufgeklebt" style="left:263px;top:268px;width:84px;height:104px;"></div>
    <div class="mask-illustration" role="img" aria-label="Fertige Einhorn-Maske mit Horn und Gummiband" style="left:428px;top:287px;width:128px;height:85px;"></div>

    <div class="step" style="left:67px;"><span class="step__num">1.</span>Maske ausschneiden</div>
    <div class="step" style="left:231px;"><span class="step__num">2.</span>Horn von hinten aufkleben</div>
    <div class="step" style="left:432px;"><span class="step__num">3.</span>Gummiband anknoten</div>

    <div class="brand-square"></div>
    <div class="wordmark">Rundblick<br>KoWeFa</div>

    <svg class="rainbow-bar" viewBox="0 0 851 17" aria-hidden="true">
      <rect x="0" width="120" height="17" fill="var(--violet)"/>
      <rect x="146" width="120" height="17" fill="var(--sky)"/>
      <rect x="293" width="120" height="17" fill="var(--green)"/>
      <rect x="439" width="120" height="17" fill="var(--yellow)"/>
      <rect x="586" width="120" height="17" fill="var(--orange)"/>
      <rect x="732" width="119" height="17" fill="var(--red)"/>
    </svg>
  </section>

  <section class="postcard postcard--plain">
    <h1 class="headline">Lesen, was den KoWeFa bewegt.<br>Die Rundblick gibt es jetzt online:</h1>
    <div class="url-band">rundblick.kowefa-beispiel.de</div>
    <p class="lead">Aktuelle Themen aus dem Landkreis und der Kreisverwaltung – auch von Zuhause,<br>unterwegs oder mit dem Smartphone abrufbar</p>
    <div class="body-copy">
      <p>Einfach Einhorn-Maske basteln, aufsetzen und den KoWeFa aus anderem Rundblick sehen.<br>Schickt uns Eure Fotos mit Einhorn-Maske an rundblick@kowefa-beispiel.de</p>
      <p>Mehr Einhorn-Masken gefällig? Die Bastelvorlage gibt es auch online.</p>
    </div>

    <div class="mask-illustration" role="img" aria-label="Einhorn-Maske mit Regenbogenmähne, ausgeschnitten" style="left:74px;top:295px;width:112px;height:72px;"></div>
    <div class="mask-illustration" role="img" aria-label="Einhorn-Maske, goldenes Horn wird von hinten aufgeklebt" style="left:287px;top:272px;width:82px;height:96px;"></div>
    <div class="mask-illustration" role="img" aria-label="Fertige Einhorn-Maske mit Horn und Gummiband" style="left:468px;top:285px;width:124px;height:82px;"></div>

    <div class="step" style="left:67px;top:372px;"><span class="step__num">1.</span>Maske ausschneiden</div>
    <div class="step" style="left:244px;top:372px;"><span class="step__num">2.</span>Horn von hinten aufkleben</div>
    <div class="step" style="left:456px;top:372px;"><span class="step__num">3.</span>Gummiband anknoten</div>

    <div class="brand-square"></div>
    <div class="wordmark">Rundblick<br>KoWeFa</div>
  </section>

</body>
</html>
```